What's wrong with sitting graphic for Pravolink

Design an info-graphic for posting to Pravolink (correct size for Pravolink) - which explains the health issues with sitting at work. Based on the attached powerpoint mock up. <br/>This can use the image 316284957 from Pixelmarsh which I can buy and send to the designer. Or designer can create own image of person sitting at a desk.

```html
<!DOCTYPE html>
<html lang="en">
<head>
<meta charset="utf-8">
<title>What are the health risks of sitting?</title>
<link rel="stylesheet" href="https://fonts.googleapis.com/css2?family=Oswald:wght@600;700&family=Roboto+Condensed:wght@400;700&display=swap">
<style>
  :root {
    --sky-top: #c6ecf8;
    --sky-mid: #e4f6fc;
    --sky-low: #d2f0fa;
    --ink: #111111;
    --orange: #f26a21;
    --navy: #12386e;
    --paper: #ffffff;
    --paper-edge: #1c1c1c;
    --tick: #2e7d32;
    --figure-a: #7fb2d9;
    --figure-b: #e39a7e;
    --lens-a: #4a5b86;
    --lens-b: #f1a23a;
    --leaf-a: #1f9a47;
    --leaf-b: #bfead0;
  }
  * { box-sizing: border-box; margin: 0; padding: 0; }
  html, body { width: 1200px; height: 1200px; overflow: hidden; }
  body {
    font-family: "Roboto Condensed", "Arial Narrow", sans-serif;
    color: var(--ink);
  }
  .poster {
    position: relative;
    width: 1200px;
    height: 1200px;
    background: linear-gradient(180deg, var(--sky-top) 0%, var(--sky-mid) 55%, var(--sky-low) 100%);
    overflow: hidden;
  }
  .headline {
    position: absolute;
    top: 30px;
    left: 0;
    width: 100%;
    text-align: center;
  }
  .headline__lead {
    font-family: "Roboto Condensed", sans-serif;
    font-weight: 700;
    font-size: 36px;
    line-height: 1.2;
  }
  .headline__main {
    font-family: "Oswald", "Impact", sans-serif;
    font-weight: 700;
    font-size: 60px;
    color: var(--orange);
    letter-spacing: 1px;
    line-height: 1.25;
  }
  .workstation-art {
    position: absolute;
    left: 95px;
    top: 283px;
    width: 600px;
    height: 604px;
    border-radius: 24px;
    background: linear-gradient(160deg, var(--figure-a) 0%, #9fc6e3 50%, var(--figure-b) 100%);
    opacity: .85;
  }
  .research-art {
    position: absolute;
    left: 764px;
    top: 283px;
    width: 200px;
    height: 150px;
    border-radius: 20px;
    background: linear-gradient(135deg, var(--lens-a) 0%, #8fa3c9 60%, var(--lens-b) 100%);
    opacity: .8;
  }
  .research-intro {
    position: absolute;
    left: 780px;
    top: 452px;
    width: 340px;
    font-weight: 700;
    font-size: 29px;
    line-height: 1.05;
    color: var(--navy);
  }
  .risk-sheet {
    position: absolute;
    left: 760px;
    top: 540px;
    width: 300px;
    height: 350px;
  }
  .risk-sheet__layer {
    position: absolute;
    inset: 0;
    background: var(--paper);
    border: 3px solid var(--paper-edge);
  }
  .risk-sheet__layer--back { transform: translate(10px, 14px) rotate(1.5deg); }
  .risk-sheet__layer--mid { transform: translate(4px, 7px) rotate(.6deg); }
  .risk-list {
    position: absolute;
    inset: 0;
    list-style: none;
    padding: 30px 0 0 44px;
  }
  .risk-list li {
    display: flex;
    align-items: center;
    gap: 14px;
    font-size: 23px;
    height: 41px;
  }
  .risk-list svg { width: 24px; height: 24px; flex: none; }
  .brand {
    position: absolute;
    left: 108px;
    top: 1050px;
    display: flex;
    align-items: center;
    gap: 12px;
  }
  .brand__mark { width: 34px; height: 34px; background: var(--navy); }
  .brand__name {
    font-weight: 700;
    font-size: 46px;
    color: var(--navy);
    line-height: 1;
  }
  .answer-bubble {
    position: absolute;
    left: 385px;
    top: 985px;
    width: 300px;
    height: 150px;
  }
  .answer {
    position: absolute;
    left: 410px;
    top: 1002px;
  }
  .answer__ask {
    font-weight: 700;
    font-size: 29px;
    color: var(--orange);
    line-height: 1.1;
  }
  .answer__call {
    font-family: "Oswald", sans-serif;
    font-weight: 600;
    font-size: 38px;
    line-height: 1.1;
    color: var(--ink);
  }
  .answer__detail {
    font-weight: 700;
    font-size: 21px;
    color: var(--navy);
  }
  .leaf-art {
    position: absolute;
    left: 990px;
    top: 985px;
    width: 160px;
    height: 170px;
    border-radius: 50% 50% 40% 40%;
    background: radial-gradient(circle at 50% 70%, var(--leaf-a) 0%, #6cc68c 45%, var(--leaf-b) 80%, transparent 100%);
    opacity: .75;
  }
</style>
</head>
<body>
<main class="poster">
  <header class="headline">
    <p class="headline__lead">What are the</p>
    <h1 class="headline__main">HEALTH RISKS OF SITTING?</h1>
  </header>

  <div class="workstation-art" role="img" aria-label="Illustration of a man sitting upright at a desk working on a computer, with posture guide markers"></div>

  <div class="research-art" role="img" aria-label="Illustration of a laptop, stacked books and a magnifying glass"></div>

  <p class="research-intro">Research connects excessive sitting with</p>

  <section class="risk-sheet">
    <div class="risk-sheet__layer risk-sheet__layer--back"></div>
    <div class="risk-sheet__layer risk-sheet__layer--mid"></div>
    <div class="risk-sheet__layer"></div>
    <ul class="risk-list">
      <li><svg viewBox="0 0 24 24"><rect x="2" y="6" width="15" height="15" fill="none" stroke="#333" stroke-width="2"/><path d="M5 13l4 4 12-14" fill="none" stroke="var(--tick)" stroke-width="3"/></svg>Cancer</li>
      <li><svg viewBox="0 0 24 24"><rect x="2" y="6" width="15" height="15" fill="none" stroke="#333" stroke-width="2"/><path d="M5 13l4 4 12-14" fill="none" stroke="var(--tick)" stroke-width="3"/></svg>Strokes</li>
      <li><svg viewBox="0 0 24 24"><rect x="2" y="6" width="15" height="15" fill="none" stroke="#333" stroke-width="2"/><path d="M5 13l4 4 12-14" fill="none" stroke="var(--tick)" stroke-width="3"/></svg>Heart attack</li>
      <li><svg viewBox="0 0 24 24"><rect x="2" y="6" width="15" height="15" fill="none" stroke="#333" stroke-width="2"/><path d="M5 13l4 4 12-14" fill="none" stroke="var(--tick)" stroke-width="3"/></svg>Type 2 diabetes</li>
      <li><svg viewBox="0 0 24 24"><rect x="2" y="6" width="15" height="15" fill="none" stroke="#333" stroke-width="2"/><path d="M5 13l4 4 12-14" fill="none" stroke="var(--tick)" stroke-width="3"/></svg>Metabolic syndrome</li>
      <li><svg viewBox="0 0 24 24"><rect x="2" y="6" width="15" height="15" fill="none" stroke="#333" stroke-width="2"/><path d="M5 13l4 4 12-14" fill="none" stroke="var(--tick)" stroke-width="3"/></svg>Premature Death</li>
      <li><svg viewBox="0 0 24 24"><rect x="2" y="6" width="15" height="15" fill="none" stroke="#333" stroke-width="2"/><path d="M5 13l4 4 12-14" fill="none" stroke="var(--tick)" stroke-width="3"/></svg>Musculoskeletal pain</li>
    </ul>
  </section>

  <div class="brand">
    <span class="brand__mark"></span>
    <span class="brand__name">restora</span>
  </div>

  <svg class="answer-bubble" viewBox="0 0 300 150" aria-hidden="true">
    <path d="M40 20 Q150 -10 260 20 Q300 75 250 125 Q150 150 50 130 L20 148 L32 118 Q0 75 40 20 Z" fill="none" stroke="#ffffff" stroke-width="3" opacity=".9"/>
    <path d="M200 30 l18 22 l40 -48" fill="none" stroke="#ffffff" stroke-width="7" opacity=".8"/>
  </svg>

  <div class="answer">
    <p class="answer__ask">The answer?</p>
    <p class="answer__call">GET MOVING</p>
    <p class="answer__detail">With a standing desk &amp; sit stand coaching software.</p>
  </div>

  <div class="leaf-art" role="img" aria-label="Decorative cluster of green leaves"></div>
</main>
</body>
</html>
```